Music Studio and Store Business Card and Logo Design

We need a business card and logo design for an existing Music Studio (Piano and Voice) which will soon expand to offer retail sheet music for all instruments including voice. The expanding store will not sell or lease instruments. We are a well known Fine Arts Studio for instruction to children, college students, and adults with 42 enrolled students and a wait list. We want something with simple elegance, but not archaic. Even a sleek modern look is okay. We do not want something childish or too fun looking because we do serve ages 5 - 62. We would also like the logo workable/transferable to signage for our new location opening in March. We like classic burgundy, black, deep blues, but are open to other suggestions. We included our studio brochure so you can get to know us a little better and some images we thought were interesting with the use of clef signs for the & and using note heads for the bottom or top of the letter "H"

Target Market(s)

All ages

Industry/Entity Type

Business

Contact Information for Business Card

K&K Music StudioPlattsburgh, NYWanda J. Haby and Osric P. Vandemeer, Owners

Requirements
Must have
• Phone Number: (555) 614-7098
• Website: www.kkfineartsstudio.example
Nice to have
• Email: lorna@kkfineartsstudio.example
Should not have
• Any instruments on the card other than piano. Instrument pix is not a necessity.

```html
<!DOCTYPE html>
<html lang="en">
<head>
<meta charset="utf-8">
<title>K&amp;K Music Studio – Business Card</title>
<link href="https://fonts.googleapis.com/css2?family=Open+Sans:wght@400;600;700&display=swap" rel="stylesheet">
<style>
  :root {
    --backdrop: #3a3431;
    --card-black: #111111;
    --card-glow: #2a2a2a;
    --stripe-white: #ffffff;
    --text-white: #ffffff;
    --text-soft: #e6e6e6;
  }
  * { box-sizing: border-box; margin: 0; padding: 0; }
  html, body {
    width: 1200px;
    height: 844px;
    overflow: hidden;
    background: var(--backdrop);
    font-family: "Open Sans", Arial, sans-serif;
  }
  .canvas {
    position: relative;
    width: 1200px;
    height: 844px;
  }
  .card {
    position: absolute;
    top: 273px;
    width: 520px;
    height: 297px;
    background: var(--card-black);
    overflow: hidden;
    box-shadow: 0 10px 28px rgba(0,0,0,0.45);
  }
  .card--info { left: 50px; }
  .card--brand {
    left: 630px;
    background: radial-gradient(ellipse 60% 70% at 45% 35%, var(--card-glow), var(--card-black) 75%);
  }

  /* Contact side: white bands along top and bottom */
  .band {
    position: absolute;
    left: 0;
    right: 0;
    height: 12px;
    background: var(--stripe-white);
  }
  .band--top { top: 0; }
  .band--bottom { bottom: 0; }

  .contact {
    position: absolute;
    left: 215px;
    top: 72px;
    color: var(--text-white);
  }
  .owner-name {
    font-weight: 700;
    font-size: 17px;
    line-height: 22px;
    letter-spacing: 0.2px;
    text-transform: uppercase;
  }
  .owner-role {
    margin-top: 4px;
    margin-left: 78px;
    font-size: 13px;
    line-height: 18px;
    color: var(--text-soft);
  }
  .details {
    margin-top: 30px;
    margin-left: 8px;
    list-style: none;
  }
  .detail {
    font-size: 14px;
    line-height: 21px;
    color: var(--text-soft);
    white-space: nowrap;
  }

  /* Brand side: white tabs at left and right edges */
  .tab {
    position: absolute;
    top: 124px;
    width: 22px;
    height: 46px;
    background: var(--stripe-white);
  }
  .tab--left { left: 0; }
  .tab--right { right: 0; }

  .brand {
    position: absolute;
    left: 0;
    right: 0;
    top: 132px;
    display: flex;
    align-items: center;
    justify-content: center;
    gap: 12px;
  }
  .brand-dot {
    width: 14px;
    height: 14px;
    border-radius: 50%;
    background: var(--text-white);
  }
  .brand-name {
    font-weight: 600;
    font-size: 24px;
    letter-spacing: 1.5px;
    color: var(--text-white);
    text-transform: uppercase;
  }
</style>
</head>
<body>
<main class="canvas">
  <section class="card card--info" aria-label="Business card, contact side">
    <div class="band band--top"></div>
    <div class="contact">
      <p class="owner-name">Lorna E. Kestrin</p>
      <p class="owner-name">Osric P. Vandemeer</p>
      <p class="owner-role">Owners</p>
      <ul class="details">
        <li class="detail">Alderbrook, NY</li>
        <li class="detail">(555) 614-7098</li>
        <li class="detail">www.kkfineartsstudio.example</li>
        <li class="detail">lorna@kkfineartsstudio.example</li>
      </ul>
    </div>
    <div class="band band--bottom"></div>
  </section>

  <section class="card card--brand" aria-label="Business card, brand side">
    <div class="tab tab--left"></div>
    <div class="brand">
      <span class="brand-dot"></span>
      <span class="brand-name">K&amp;K Music Studio</span>
    </div>
    <div class="tab tab--right"></div>
  </section>
</main>
</body>
</html>
```